Eye catching Stationary Design

Healthcare consultant firm looking for stationary design ( letterhead, envelope and business cards) That’s professional, classy and eye catching . The design should incorporate the logo and the colors of the logo in its design. You can see the logo on our website at www harbor key advisors. com.

```html
<!DOCTYPE html>
<html lang="en">
<head>
<meta charset="utf-8">
<title>Harbor Key Advisors – Envelope</title>
<link href="https://fonts.googleapis.com/css2?family=PT+Sans&family=Saira+Condensed:wght@400;500&display=swap" rel="stylesheet">
<style>
  :root {
    --brand-blue: #0455a5;
    --sky-blue: #36a3d5;
    --navy: #10306f;
    --paper: #ffffff;
    --bg-dark: #a9a8a9;
    --bg-light: #f6f6f6;
  }
  * { margin: 0; padding: 0; box-sizing: border-box; }
  html, body { width: 849px; height: 1200px; overflow: hidden; }
  body {
    position: relative;
    background: linear-gradient(160deg, var(--bg-dark) 0%, #d4d3d4 55%, var(--bg-light) 100%);
    font-family: "Saira Condensed", sans-serif;
  }
  .envelope {
    position: absolute;
    left: 113px;
    width: 623px;
    height: 393px;
    background: var(--paper);
    box-shadow: 6px 6px 10px rgba(0,0,0,0.35);
    overflow: hidden;
  }
  .envelope--front { top: 28px; }
  .envelope--back { top: 627px; }

  .side-band {
    position: absolute; left: 0; top: 0;
    width: 38px; height: 100%;
    background: var(--brand-blue);
  }
  .side-band__name {
    position: absolute;
    left: 19px; top: 197px;
    transform: translate(-50%, -50%) rotate(-90deg);
    white-space: nowrap;
    font-size: 24px;
    font-weight: 400;
    letter-spacing: 0.3px;
    color: var(--navy);
  }
  .brand-name {
    position: absolute;
    font-weight: 500;
    white-space: nowrap;
    text-transform: uppercase;
    letter-spacing: 0.6px;
  }
  .envelope--front .brand-name {
    right: 12px; top: 30px;
    font-size: 13px;
    color: var(--brand-blue);
  }
  .rule { position: absolute; right: 0; height: 3px; }
  .rule--light { top: 55px; width: 331px; background: var(--sky-blue); }
  .rule--dark { top: 63px; width: 367px; background: var(--brand-blue); }

  .flap {
    position: absolute; left: 0; top: 0;
    width: 100%; height: 123px;
    background: var(--brand-blue);
    border-radius: 0 0 55px 55px;
  }
  .flap .brand-name {
    left: 50%; top: 62px;
    transform: translateX(-50%);
    font-size: 14px;
    color: var(--navy);
  }
  .contact-band {
    position: absolute; left: 0; top: 358px;
    width: 100%; height: 14px;
    background: var(--brand-blue);
  }
  .pattern-strip {
    position: absolute; left: 0; top: 373px;
    width: 100%; height: 20px;
    background: linear-gradient(180deg, #6c95c8, #4f80bd);
  }
  .contact {
    position: absolute; top: 344px;
    display: flex; align-items: center;
    height: 28px;
  }
  .contact__icon {
    width: 26px; height: 26px;
    border-radius: 50%;
    background: var(--brand-blue);
    display: flex; align-items: center; justify-content: center;
    margin-right: 9px;
  }
  .contact__text {
    color: var(--paper);
    font-size: 11px;
    margin-top: 13px;
    white-space: nowrap;
  }
  .contact--address { left: 9px; }
  .contact--phone { left: 266px; }
  .contact--web { left: 436px; }

  .label {
    position: absolute; left: 183px; width: 483px;
    text-align: center;
  }
  .label__bar { height: 13px; background: var(--brand-blue); }
  .label__text {
    font-family: "PT Sans", sans-serif;
    font-size: 56px;
    line-height: 67px;
    color: var(--brand-blue);
  }
  .label--front { top: 458px; }
  .label--back { top: 1078px; }
</style>
</head>
<body>
  <section class="envelope envelope--front">
    <div class="side-band"><span class="side-band__name">Harbor Key Advisors</span></div>
    <span class="brand-name">Harbor Key Advisors LLC</span>
    <div class="rule rule--light"></div>
    <div class="rule rule--dark"></div>
  </section>

  <div class="label label--front">
    <div class="label__bar"></div>
    <div class="label__text">Envelope Front</div>
    <div class="label__bar"></div>
  </div>

  <section class="envelope envelope--back">
    <div class="flap"><span class="brand-name">Harbor Key Advisors LLC</span></div>
    <div class="contact-band"></div>
    <div class="pattern-strip" role="img" aria-label="Band of small blue squares along the bottom edge"></div>

    <div class="contact contact--address">
      <span class="contact__icon">
        <svg width="16" height="16" viewBox="0 0 16 16"><path d="M8 2 L15 8 H13 V14 H10 V10 H6 V14 H3 V8 H1 Z" fill="#fff"/></svg>
      </span>
      <span class="contact__text">88 Lantern Row Ste 12, Portvale, NY 10990, USA</span>
    </div>
    <div class="contact contact--phone">
      <span class="contact__icon">
        <svg width="16" height="16" viewBox="0 0 16 16"><path d="M3 1.5 L6 1.5 L7 5 L5.2 6.4 C6 8.3 7.7 10 9.6 10.8 L11 9 L14.5 10 L14.5 13 C14.5 14 13.6 14.6 12.6 14.5 C6.8 13.8 2.2 9.2 1.5 3.4 C1.4 2.4 2 1.5 3 1.5 Z" fill="#fff"/></svg>
      </span>
      <span class="contact__text">(555) 014-2290</span>
    </div>
    <div class="contact contact--web">
      <span class="contact__icon">
        <svg width="16" height="16" viewBox="0 0 16 16" fill="none" stroke="#fff" stroke-width="1.2"><circle cx="8" cy="8" r="6.5"/><ellipse cx="8" cy="8" rx="3" ry="6.5"/><path d="M1.5 8 H14.5 M2.5 4.5 H13.5 M2.5 11.5 H13.5"/></svg>
      </span>
      <span class="contact__text">https://www.harborkeyadvisors.com</span>
    </div>
  </section>

  <div class="label label--back">
    <div class="label__bar"></div>
    <div class="label__text">Envelope Back</div>
    <div class="label__bar"></div>
  </div>
</body>
</html>
```